Oven Cleaning Business owner needs business card design

Hi there,
Would like for a business card to be designed for myself, the owner of a professional oven cleaning business on the Sunshine Coast.
Would like it to look sleek, and modern-ish. Bit creative is encouraged too.
Include following:
Name/title: Corin de Walbrek, Owner
Phone number: 1300 482 906
Email: info@kitchenlustrely.com.au
Website: www.kitchenlustrely.com.au

```html
<!DOCTYPE html>
<html lang="en">
<head>
<meta charset="utf-8">
<title>Kitchen Lustrely – Business Card</title>
<link href="https://fonts.googleapis.com/css2?family=Outfit:wght@400;500;600;700&family=Montserrat:wght@400;500&display=swap" rel="stylesheet">
<style>
  :root {
    --backdrop: #c4c4c4;
    --turquoise: #1adbdb;
    --turquoise-deep: #17c9cd;
    --mist: #dcfcfd;
    --foam: #f3fefe;
    --bubble: #7fd9e3;
    --navy: #161d3c;
    --ink: #0b0b0b;
    --white: #ffffff;
  }
  * { box-sizing: border-box; margin: 0; padding: 0; }
  html, body { width: 1200px; height: 904px; overflow: hidden; }
  body {
    background: var(--backdrop);
    position: relative;
    font-family: "Outfit", sans-serif;
    color: var(--ink);
  }
  .card {
    position: absolute;
    width: 473px;
    height: 271px;
    overflow: hidden;
    box-shadow: 0 2px 6px rgba(0,0,0,.18);
  }

  /* Front */
  .card-front { left: 198px; top: 157px; background: var(--turquoise); }
  .front-foam {
    position: absolute; left: 0; top: 138px; width: 100%; height: 133px;
    background: linear-gradient(180deg, rgba(127,217,227,0) 0%, var(--bubble) 30%, #a9e8ee 60%, var(--foam) 78%, var(--foam) 100%);
  }
  .front-brand {
    position: absolute; top: 60px; left: 0; width: 100%;
    display: flex; flex-direction: column; align-items: center; gap: 10px;
  }
  .brand-dot {
    width: 58px; height: 58px; border-radius: 50%; background: var(--white); flex: none;
  }
  .brand-name {
    font-weight: 700; font-size: 26px; letter-spacing: 2px;
    color: var(--white); text-transform: uppercase; white-space: nowrap;
  }
  .front-web {
    position: absolute; left: 0; width: 100%; top: 239px; text-align: center;
    font-family: "Montserrat", sans-serif; font-size: 11.5px; letter-spacing: 1.6px;
    color: #222;
  }

  /* Back */
  .card-back { left: 529px; top: 476px; background: var(--mist); }
  .back-foam {
    position: absolute; left: 0; top: 120px; width: 100%; height: 90px;
    background: linear-gradient(180deg, rgba(255,255,255,0) 0%, rgba(255,255,255,.85) 100%);
  }
  .back-wave { position: absolute; left: 0; top: 0; width: 473px; height: 271px; }
  .owner-photo {
    position: absolute; left: 214px; top: 18px; width: 200px; height: 253px;
    background: linear-gradient(180deg, #19d3d8 0%, #17c6cc 45%, #1b2447 62%, var(--navy) 100%);
    border-radius: 50% 50% 0 0 / 30% 30% 0 0;
  }
  .owner-name { position: absolute; left: 33px; top: 52px; font-weight: 600; font-size: 16px; }
  .owner-title { position: absolute; left: 33px; top: 73px; font-weight: 500; font-size: 13px; color: var(--turquoise-deep); }
  .contact-list { position: absolute; left: 33px; top: 92px; list-style: none; }
  .contact-item {
    display: flex; align-items: center; gap: 6px; height: 17px;
    font-size: 11px; font-weight: 500;
  }
  .contact-icon { width: 12px; height: 12px; flex: none; }
  .back-brand {
    position: absolute; left: 24px; top: 222px;
    display: flex; align-items: center; gap: 7px;
  }
  .back-brand .brand-dot { width: 28px; height: 28px; }
  .back-brand .brand-name { font-size: 13px; color: var(--ink); letter-spacing: 1px; }
</style>
</head>
<body>
  <section class="card card-front">
    <div class="front-foam" role="img" aria-label="Band of soap bubbles and foam across the lower card"></div>
    <div class="front-brand">
      <span class="brand-dot"></span>
      <span class="brand-name">Kitchen Lustrely</span>
    </div>
    <p class="front-web">www.kitchenlustrely.com.au</p>
  </section>

  <section class="card card-back">
    <div class="back-foam" role="img" aria-label="Soft soap bubble foam behind the contact details"></div>
    <svg class="back-wave" viewBox="0 0 473 271" aria-hidden="true">
      <path d="M0 200 Q95 170 230 214 L230 271 L0 271 Z" fill="var(--turquoise)"/>
      <path d="M0 200 Q95 170 230 214" fill="none" stroke="var(--ink)" stroke-width="5"/>
      <path d="M400 220 Q440 210 473 190 L473 271 L400 271 Z" fill="var(--turquoise)"/>
      <path d="M400 214 Q440 205 473 184" fill="none" stroke="var(--ink)" stroke-width="5"/>
    </svg>
    <div class="owner-photo" role="img" aria-label="Photo of the owner in a navy polo giving a thumbs up"></div>

    <h1 class="owner-name">Corin de Walbrek,</h1>
    <p class="owner-title">OWNER</p>
    <ul class="contact-list">
      <li class="contact-item">
        <svg class="contact-icon" viewBox="0 0 12 12"><circle cx="6" cy="6" r="6" fill="var(--turquoise)"/><path d="M4 3.2 5 4.6 4.4 5.3Q5.2 6.8 6.7 7.6L7.4 7 8.8 8 8.2 8.9Q5.4 8.6 3.1 3.8Z" fill="#fff"/></svg>
        1300 482 906
      </li>
      <li class="contact-item">
        <svg class="contact-icon" viewBox="0 0 12 12"><circle cx="6" cy="6" r="6" fill="var(--turquoise)"/><rect x="3" y="4" width="6" height="4.2" fill="none" stroke="#fff" stroke-width=".9"/><path d="M3 4 6 6.3 9 4" fill="none" stroke="#fff" stroke-width=".9"/></svg>
        info@kitchenlustrely.com.au
      </li>
      <li class="contact-item">
        <svg class="contact-icon" viewBox="0 0 12 12"><circle cx="6" cy="6" r="6" fill="var(--turquoise)"/><circle cx="6" cy="6" r="3.2" fill="none" stroke="#fff" stroke-width=".8"/><ellipse cx="6" cy="6" rx="1.4" ry="3.2" fill="none" stroke="#fff" stroke-width=".8"/><path d="M2.8 6H9.2" stroke="#fff" stroke-width=".8"/></svg>
        www.kitchenlustrely.com.au
      </li>
    </ul>

    <div class="back-brand">
      <span class="brand-dot"></span>
      <span class="brand-name">Kitchen Lustrely</span>
    </div>
  </section>
</body>
</html>
```